The Queen Rides Again Line of Sparkling Wine & Spirits

Back info: Tara Joy Whitfield Owner 209-555-0143 1700 E. Harlowe Rd, Bldg. 2, & 3, Alder Ca. 95111
Fine Bubbles & Keepsakes www.thequeenridesagain.example
Ok I have uploaded the winning design. The color that I am after is the Fushia, Raspberry, Red, Matte Satin Matalic Finish. With a 24 Karet Gold color Foil. The Bottle is on the top row and it's the 2nd Bottle in. That is the Color that I want. This is the style of font. Make sure that you put what we're advertising. Good Luck to you all. Warmest regards, Tara
Target Market(s)
21 & up UniSex
Industry/Entity Type
Sparkling Wine and Memorabilia
Contact Information for Business Card
there listed up above.....
Look and feel

```html
<!DOCTYPE html>
<html lang="en">
<head>
<meta charset="utf-8">
<title>The Queen Rides Again — Business Card</title>
<link href="https://fonts.googleapis.com/css2?family=Poppins:wght@400;600&display=swap" rel="stylesheet">
<style>
  :root {
    --stage: #2a2b2e;
    --fuchsia-deep: #a8125f;
    --fuchsia: #e0138f;
    --fuchsia-bright: #f217a0;
    --gold-dark: #b8861f;
    --gold: #d9ac45;
    --gold-light: #f6d98a;
    --ink: #111111;
    --paper-text: #fbe9f4;
  }
  * { box-sizing: border-box; margin: 0; padding: 0; }
  html, body { width: 1200px; height: 952px; overflow: hidden; }
  body {
    background: var(--stage);
    position: relative;
    font-family: "Poppins", Arial, sans-serif;
  }
  .card {
    position: absolute;
    width: 540px;
    height: 308px;
    border-radius: 4px;
    overflow: hidden;
    background: linear-gradient(135deg, var(--fuchsia-deep) 0%, var(--fuchsia) 45%, var(--fuchsia-bright) 60%, var(--fuchsia-deep) 100%);
    box-shadow: 0 14px 30px rgba(0,0,0,.45);
  }
  .gold-foil {
    background: linear-gradient(120deg, var(--gold-dark) 0%, var(--gold) 45%, var(--gold-light) 100%);
  }

  /* Front */
  .card-front { left: 620px; top: 150px; }
  .brand-band {
    position: absolute;
    left: 100px; top: 84px;
    width: 340px; height: 140px;
    border-radius: 70px;
    display: flex; align-items: center; justify-content: center;
  }
  .brand-name {
    font-family: "Poppins", Arial, sans-serif;
    font-weight: 600;
    font-size: 30px;
    line-height: 1.2;
    color: var(--ink);
    text-align: center;
    width: 260px;
  }

  /* Back */
  .card-back { left: 40px; top: 490px; }
  .name-tab {
    position: absolute;
    left: 0; top: 24px;
    width: 290px; height: 66px;
    border-radius: 0 33px 33px 0;
    border: 2px solid var(--ink);
    border-left: none;
    padding: 9px 0 0 40px;
  }
  .holder-name {
    font-weight: 600;
    font-size: 22px;
    line-height: 1.1;
    color: var(--ink);
    letter-spacing: .5px;
    white-space: nowrap;
  }
  .holder-title {
    font-size: 13px;
    line-height: 1.3;
    color: var(--ink);
  }
  .contact-list {
    position: absolute;
    left: 40px; top: 108px;
    list-style: none;
    color: var(--paper-text);
    font-size: 10.5px;
    line-height: 1.3;
  }
  .contact-list li { display: flex; align-items: flex-start; gap: 8px; margin-bottom: 6px; }
  .icon {
    flex: none;
    width: 14px; height: 14px;
    background: var(--ink);
    border-radius: 2px;
    display: flex; align-items: center; justify-content: center;
  }
  .icon svg { width: 10px; height: 10px; }
  .social-row { align-items: center; gap: 10px; margin-top: 2px; font-size: 9px; }
  .social { display: flex; align-items: center; gap: 4px; }
  .social-box { width: 12px; height: 12px; border-radius: 2px; }
  .tagline { font-size: 9px; font-weight: 600; color: var(--paper-text); }
  .brand-mark {
    position: absolute;
    right: 40px; bottom: 34px;
    width: 170px;
    display: flex; flex-direction: column; align-items: center; gap: 10px;
  }
  .mark-dot {
    width: 64px; height: 64px;
    border-radius: 50%;
    background: var(--ink);
  }
  .mark-name {
    font-weight: 600;
    font-size: 15px;
    color: var(--ink);
    text-align: center;
    line-height: 1.25;
  }
</style>
</head>
<body>

  <section class="card card-front" aria-label="Card front">
    <div class="brand-band gold-foil">
      <p class="brand-name">The Queen Rides Again</p>
    </div>
  </section>

  <section class="card card-back" aria-label="Card back">
    <div class="name-tab gold-foil">
      <p class="holder-name">TARA WHITFIELD</p>
      <p class="holder-title">Owner</p>
    </div>

    <ul class="contact-list">
      <li>
        <span class="icon">
          <svg viewBox="0 0 10 10"><path d="M5 0.8a3 3 0 0 1 3 3c0 2.2-3 5.4-3 5.4S2 6 2 3.8a3 3 0 0 1 3-3z" fill="#d9ac45"/><circle cx="5" cy="3.8" r="1.1" fill="#111"/></svg>
        </span>
        <span>1700 E. Harlowe Rd, Bldg. 2, &amp; 3,<br>Alder Ca. 95111</span>
      </li>
      <li>
        <span class="icon">
          <svg viewBox="0 0 10 10"><path d="M2.4 1l1.6 1.8-.9 1.2c.6 1.2 1.6 2.2 2.9 2.9l1.2-.9L9 7.6 8 9C4.4 8.7 1.3 5.6 1 2z" fill="#d9ac45"/></svg>
        </span>
        <span>209-555-0143</span>
      </li>
      <li>
        <span class="icon">
          <svg viewBox="0 0 10 10"><rect x="1" y="2.2" width="8" height="5.6" fill="none" stroke="#d9ac45" stroke-width="1"/><path d="M1 2.4l4 3 4-3" fill="none" stroke="#d9ac45" stroke-width="1"/></svg>
        </span>
        <span>hello@thequeenridesagain.example</span>
      </li>
      <li>
        <span class="icon">
          <svg viewBox="0 0 10 10"><path d="M5 1l3.5 8L5 7 1.5 9z" fill="#d9ac45"/></svg>
        </span>
        <span>www.thequeenridesagain.example</span>
      </li>
      <li class="social-row">
        <span class="social"><span class="social-box gold-foil"></span>Facetome</span>
        <span class="social"><span class="social-box gold-foil"></span>Picstream</span>
      </li>
      <li class="tagline">Fine Bubbles &amp; Keepsakes</li>
    </ul>

    <div class="brand-mark">
      <span class="mark-dot"></span>
      <p class="mark-name">The Queen Rides Again</p>
    </div>
  </section>

</body>
</html>
```